Book Cover Design on Conflict resolution

I need a book cover design for the following book title. Title: "The Craft of Accord: Steering Disputes with Candor, Social Awareness, and Steadfastness" The author's name is Marcus Dellway. The book covers multiple areas to include unconscious bias, retaliation and reprisal. I am interested in seeing the designs that provide a unique eye catching presence.

Target Market(s)

Organizations and major corporations. Personal conflicts and self help. Federal Government, Schools, and Churches

Industry/Entity Type

Large Corporation, Federal Government, Churches, Schools

Font styles to use
Serif

Colors
0054AA
0677BA
7BADD7
CADEEF
E8F1F8
59FF00
82FF00
B8FF75
E3FFCB
F4FFEA

Requirements
Nice to have
• something unique and creative

```html
<!DOCTYPE html>
<html lang="en">
<head>
<meta charset="utf-8">
<title>The Craft of Accord — Marcus Dellway</title>
<link href="https://fonts.googleapis.com/css2?family=Bebas+Neue&family=EB+Garamond:wght@500;600&display=swap" rel="stylesheet">
<style>
  :root {
    --ink-deep: #17527a;
    --ink-bright: #1a7fb0;
    --paper: #ffffff;
  }
  html, body {
    margin: 0;
    padding: 0;
    width: 800px;
    height: 1200px;
    overflow: hidden;
    background: var(--paper);
  }
  .cover {
    position: relative;
    width: 800px;
    height: 1200px;
    background: var(--paper);
    overflow: hidden;
  }
  .author {
    position: absolute;
    top: 50px;
    left: 0;
    width: 100%;
    margin: 0;
    text-align: center;
    font-family: "EB Garamond", serif;
    font-weight: 600;
    font-size: 34px;
    letter-spacing: 0.32em;
    padding-left: 0.32em;
    box-sizing: border-box;
    color: var(--ink-bright);
    text-transform: uppercase;
  }
  .title {
    position: absolute;
    top: 180px;
    left: 0;
    width: 100%;
    margin: 0;
    text-align: center;
    color: var(--ink-deep);
    font-weight: normal;
  }
  .title__line {
    display: block;
    font-family: "Bebas Neue", sans-serif;
    font-size: 140px;
    line-height: 1;
  }
  .title__line--top {
    letter-spacing: 0.12em;
    padding-left: 0.12em;
  }
  .title__line--bottom {
    letter-spacing: 0.34em;
    padding-left: 0.34em;
    margin-top: -4px;
  }
  .title__joiner {
    display: block;
    font-family: "EB Garamond", serif;
    font-weight: 600;
    font-size: 38px;
    line-height: 1;
    letter-spacing: 0.2em;
    padding-left: 0.2em;
    margin: 14px 0 8px;
  }
  .subtitle {
    position: absolute;
    top: 560px;
    left: 0;
    width: 100%;
    margin: 0;
    text-align: center;
    font-family: "EB Garamond", serif;
    font-weight: 600;
    font-size: 25px;
    line-height: 46px;
    color: var(--ink-bright);
    text-transform: uppercase;
  }
  .subtitle span { display: block; }
  .scene {
    position: absolute;
    left: 0;
    top: 765px;
    width: 800px;
    height: 435px;
    background: linear-gradient(to bottom, rgba(23, 82, 122, 0) 0%, rgba(23, 82, 122, 0.55) 25%, var(--ink-deep) 55%);
  }
</style>
</head>
<body>
  <main class="cover">
    <p class="author">Marcus Dellway</p>
    <h1 class="title">
      <span class="title__line title__line--top">The Craft</span>
      <span class="title__joiner">OF</span>
      <span class="title__line title__line--bottom">Accord</span>
    </h1>
    <p class="subtitle">
      <span>Steering Disputes with Candor</span>
      <span>Social Awareness and Steadfastness</span>
    </p>
    <div class="scene" role="img" aria-label="Dark blue silhouettes of two people facing away from each other, with a small figure standing between them, arms spread wide"></div>
  </main>
</body>
</html>
```